Destination Wedding Photographer

I am a Wedding photographer based in San Juan, Puerto Rico. The banner will be shown in the United States to brides that plan to have their wedding in Puerto Rico.

I want to highlight the following words/phrases
Puerto Rico
Destination Wedding
Photographer
(in that order)

feel free to get creative adding your own inspired text.

My web site: www.renzomalvek.com

Target Market(s)

Brides in the united states looking for a photographer for their wedding in Puerto Rico

Industry/Entity Type

Wedding

Requirements
Must have
• + Your ad must be a .gif, .png or .jpg smaller than 40kb in filesize
+ include the following sizes: 300x250, 728x90, 160x600, 468x60, or 120x600
+ Your ad must include the advertiser's brand
+ Your ad must have a border
Should not have
• + Your ad cannot imitate computer effects like scrolling or mousing over
+ No animations longer than 30 seconds
+ No strobe or flashing effects allowed
+ Your ad and campaign must not feature or promote alcohol, anabolic steroids, drugs, financial products, gambling, adult content, or weight loss products

```html
<!DOCTYPE html>
<html lang="en">
<head>
<meta charset="utf-8">
<title>Renzo Malvek Photography – Web Banner Set</title>
<link rel="stylesheet" href="https://fonts.googleapis.com/css2?family=Roboto+Condensed:wght@700&family=Cookie&family=Caveat:wght@400&display=swap">
<style>
  :root {
    --page: #f3f5f7;
    --banner: #3b3633;
    --banner-edge: #1f1c1a;
    --teal: #1aa497;
    --pink: #ef5f9c;
    --btn-top: #fdc04a;
    --btn-bottom: #f29a1a;
    --white: #ffffff;
    --ink: #262422;
    --label: #9a9da1;
    --photo-a: #c99a6a;
    --photo-b: #7fa7c9;
    --photo-c: #6e5a48;
  }
  * { margin: 0; padding: 0; box-sizing: border-box; }
  html, body { width: 1200px; height: 1200px; overflow: hidden; }
  body {
    background: radial-gradient(circle at 50% 40%, #ffffff 0%, var(--page) 70%, #e9ecef 100%);
    position: relative;
    font-family: "Roboto Condensed", "Arial Narrow", sans-serif;
  }
  .size-label {
    position: absolute;
    font-family: "Caveat", cursive;
    font-size: 17px;
    color: var(--label);
    letter-spacing: 1px;
  }
  .banner {
    position: absolute;
    background:
      repeating-linear-gradient(135deg, rgba(255,255,255,0.025) 0 2px, transparent 2px 6px),
      linear-gradient(180deg, #45403c 0%, var(--banner) 60%, #302c29 100%);
    border: 1px solid var(--banner-edge);
    overflow: hidden;
  }
  .banner > * { position: absolute; }
  .centered { left: 0; width: 100%; text-align: center; }
  .brand {
    color: var(--white);
    font-weight: 700;
    line-height: 1;
    white-space: nowrap;
    letter-spacing: 1px;
  }
  .region {
    color: var(--teal);
    font-weight: 700;
    line-height: 1;
    white-space: nowrap;
    text-shadow: 0 1px 1px rgba(0,0,0,0.5);
  }
  .rule { height: 2px; background: var(--teal); }
  .wedding {
    font-family: "Cookie", cursive;
    color: var(--pink);
    line-height: 1;
    white-space: nowrap;
  }
  .role {
    color: var(--pink);
    font-weight: 700;
    line-height: 1;
    white-space: nowrap;
    text-shadow: 0 1px 1px rgba(0,0,0,0.5);
  }
  .cta {
    display: flex; align-items: center; justify-content: center;
    color: var(--white);
    font-weight: 700;
    border-radius: 10px;
    background: linear-gradient(180deg, var(--btn-top), var(--btn-bottom));
    box-shadow: 0 3px 0 #b86d0c, 0 4px 6px rgba(0,0,0,0.45);
    text-shadow: 0 1px 1px rgba(0,0,0,0.35);
    white-space: nowrap;
  }
  .photo-collage {
    background: linear-gradient(135deg, var(--photo-a) 0%, var(--photo-b) 45%, var(--photo-c) 100%);
    border: 3px solid var(--white);
    box-shadow: 0 3px 8px rgba(0,0,0,0.6);
  }
  .main-logo {
    position: absolute;
    left: 550px; top: 470px; width: 560px;
    text-align: center;
    color: var(--ink);
    font-size: 78px;
    font-weight: 700;
    letter-spacing: 4px;
    line-height: 1;
  }
</style>
</head>
<body>

  <!-- Leaderboard -->
  <div class="size-label" style="left:148px;top:148px;">728x90 px</div>
  <section class="banner" style="left:149px;top:177px;width:728px;height:90px;">
    <div class="brand" style="left:12px;top:36px;font-size:18px;">RENZO MALVEK</div>
    <div class="photo-collage" role="img" aria-label="Tilted collage of wedding photos: bride portrait, couple embracing, colonial dome in San Juan" style="left:152px;top:4px;width:240px;height:82px;"></div>
    <div class="region" style="left:404px;top:7px;font-size:28px;">PUERTO RICO</div>
    <div class="cta" style="left:432px;top:45px;width:126px;height:32px;font-size:15px;">HIRE ME NOW!</div>
    <div class="wedding" style="left:576px;top:4px;font-size:46px;">Wedding</div>
    <div class="role" style="left:584px;top:56px;font-size:22px;">Photographer</div>
  </section>

  <!-- Full banner -->
  <div class="size-label" style="left:148px;top:288px;">468x60 px</div>
  <section class="banner" style="left:149px;top:317px;width:468px;height:60px;">
    <div class="brand" style="left:9px;top:24px;font-size:12px;">RENZO MALVEK</div>
    <div class="photo-collage" role="img" aria-label="Tilted collage of wedding photos: bride portrait, couple embracing, colonial dome in San Juan" style="left:104px;top:3px;width:164px;height:54px;"></div>
    <div class="region" style="left:359px;top:8px;font-size:18px;">PUERTO RICO</div>
    <div class="wedding" style="left:276px;top:17px;font-size:34px;">Wedding</div>
    <div class="role" style="left:373px;top:28px;font-size:15px;">Photographer</div>
  </section>

  <!-- Wide skyscraper -->
  <div class="size-label" style="left:148px;top:398px;">160x600 px</div>
  <section class="banner" style="left:149px;top:427px;width:160px;height:600px;">
    <div class="brand centered" style="top:44px;font-size:19px;">RENZO MALVEK</div>
    <div class="region centered" style="top:101px;font-size:27px;">PUERTO RICO</div>
    <div class="rule" style="left:7px;top:131px;width:146px;"></div>
    <div class="wedding centered" style="top:140px;font-size:50px;">Wedding</div>
    <div class="role centered" style="top:194px;font-size:22px;">Photographer</div>
    <div class="photo-collage" role="img" aria-label="Stacked wedding photos: bride portrait, colonial dome, couple kissing under arches" style="left:4px;top:232px;width:152px;height:292px;"></div>
    <div class="cta" style="left:16px;top:545px;width:128px;height:32px;font-size:15px;">HIRE ME NOW!</div>
  </section>

  <!-- Skyscraper -->
  <div class="size-label" style="left:338px;top:398px;">120x600 px</div>
  <section class="banner" style="left:339px;top:427px;width:120px;height:600px;">
    <div class="brand centered" style="top:32px;font-size:13px;letter-spacing:0.5px;">RENZO MALVEK</div>
    <div class="region centered" style="top:70px;font-size:27px;">PUERTO<br>RICO</div>
    <div class="rule" style="left:16px;top:129px;width:88px;"></div>
    <div class="wedding centered" style="top:138px;font-size:40px;">Wedding</div>
    <div class="role centered" style="top:182px;font-size:18px;">Photographer</div>
    <div class="photo-collage" role="img" aria-label="Stacked wedding photos: bride portrait, colonial dome, couple kissing under arches" style="left:3px;top:232px;width:114px;height:292px;"></div>
    <div class="cta" style="left:6px;top:558px;width:107px;height:28px;font-size:13px;">HIRE ME NOW!</div>
  </section>

  <!-- Medium rectangle -->
  <div class="size-label" style="left:490px;top:740px;">300x250 px</div>
  <section class="banner" style="left:490px;top:777px;width:300px;height:250px;">
    <div class="brand" style="left:144px;top:22px;font-size:17px;">RENZO MALVEK</div>
    <div class="photo-collage" role="img" aria-label="Stacked wedding photos: bride portrait, colonial dome, couple kissing" style="left:3px;top:10px;width:98px;height:236px;"></div>
    <div class="region" style="left:108px;top:76px;font-size:31px;">PUERTO RICO</div>
    <div class="rule" style="left:108px;top:110px;width:177px;"></div>
    <div class="wedding" style="left:146px;top:116px;font-size:50px;">Wedding</div>
    <div class="role" style="left:154px;top:172px;font-size:22px;">Photographer</div>
    <div class="cta" style="left:158px;top:204px;width:126px;height:32px;font-size:15px;">HIRE ME NOW!</div>
  </section>

  <!-- Brand mark -->
  <div class="main-logo">RENZO MALVEK</div>

</body>
</html>
```